21 ERP project mistakes to avoid

I am looking for a document template for a white paper of about 20 pages that discusses 21 mistakes you can make when selecting or implementing erp software. The audience is corporate - typically managers charged with leading an erp selection or implementation project. I want something modern and minimalist. I,m assuming the template would need to be in MS Word but the delivery format would be PDF. This not really a brochure but there is no closer category to this on the site.

Target Market(s)

Corporate enterprise software managers

Font styles to use
Serif
Sans Serif

Colors
0493ce

Requirements
Must have
• Modern,minimalist look. MS Word template or a template I can imoprt text into and convert to PDF for publishing via a web link to the document
Nice to have
• Creative front page and headings for each piece of '21 mistakes' content.plenty of white space in design.
Should not have
• Lots of crammed text and boring headings

```html
<!DOCTYPE html>
<html lang="en">
<head>
<meta charset="utf-8">
<title>21 mistakes about ERP software selection</title>
<link href="https://fonts.googleapis.com/css2?family=Lato:wght@300;400;700&display=swap" rel="stylesheet">
<style>
  :root {
    --sky: #00b6ec;
    --amber: #fbb040;
    --paper: #ffffff;
    --heading-blue: #2b7dc5;
    --ink: #2e2e2e;
  }
  html, body {
    margin: 0;
    padding: 0;
    overflow: hidden;
  }
  body {
    width: 848px;
    height: 1200px;
    font-family: "Lato", sans-serif;
  }
  .page {
    position: relative;
    width: 848px;
    height: 1200px;
    overflow: hidden;
    background: var(--sky);
  }
  .page-backdrop {
    position: absolute;
    inset: 0;
    width: 848px;
    height: 1200px;
  }
  .title {
    margin: 0;
    color: var(--paper);
    font-weight: 400;
    text-shadow: 0 1px 3px rgba(0,0,0,0.18);
  }
  .title-line {
    position: absolute;
    display: block;
    white-space: nowrap;
    font-size: 40px;
    line-height: 48px;
  }
  .title-line--first {
    right: 70px;
    top: 114px;
  }
  .title-line--second {
    left: 243px;
    top: 157px;
  }
  .title-strong {
    font-weight: 700;
    font-size: 47px;
  }
  .intro {
    position: absolute;
    top: 214px;
    left: 0;
    right: 22px;
    margin: 0;
    font-size: 14.8px;
    line-height: 21.7px;
    font-weight: 300;
    color: var(--ink);
  }
  .intro-line {
    display: block;
    text-align: justify;
    text-align-last: justify;
    white-space: nowrap;
  }
  .intro-line--last {
    text-align-last: left;
  }
  .mistake-heading {
    position: absolute;
    left: 0;
    right: 0;
    margin: 0 auto;
    width: max-content;
    font-size: 28px;
    line-height: 32px;
    font-weight: 700;
    color: var(--heading-blue);
    border-bottom: 2px solid var(--amber);
    padding-bottom: 0;
  }
  .mistake-body {
    position: absolute;
    left: 126px;
    width: 598px;
    margin: 0;
    font-size: 15px;
    line-height: 20.8px;
    font-weight: 300;
    color: var(--ink);
    text-align: justify;
    text-align-last: center;
  }
</style>
</head>
<body>
<main class="page">
  <svg class="page-backdrop" viewBox="0 0 848 1200" aria-hidden="true">
    <defs>
      <clipPath id="amber-sweep-clip">
        <path d="M848,0 C520,0 150,100 0,372 L0,1200 L30,1200 C420,1160 745,995 848,772 Z"/>
      </clipPath>
    </defs>
    <path class="amber-sweep" fill="var(--amber)"
          d="M848,0 C520,0 150,100 0,372 L0,1200 L30,1200 C420,1160 745,995 848,772 Z"/>
    <path class="paper-sheet" fill="var(--paper)"
          d="M848,8 C530,10 165,118 0,398 L0,1200 L60,1200 C430,1150 740,990 848,800 Z"/>
    <rect class="title-band" x="0" y="115" width="848" height="91"
          fill="var(--amber)" clip-path="url(#amber-sweep-clip)"/>
  </svg>

  <h1 class="title">
    <span class="title-line title-line--first"><span class="title-strong">21</span> mistakes about <span class="title-strong">ERP</span></span>
    <span class="title-line title-line--second">software selection</span>
  </h1>

  <p class="intro">
    <span class="intro-line" style="margin-left:183px">"Lorem ipsum dolor sit amet, consectetur adipiscing elit, sed do eiusmod tempor</span>
    <span class="intro-line" style="margin-left:157px">incididunt ut labore et dolore magna aliqua. Ut enim ad minim veniam, quis nostrud</span>
    <span class="intro-line" style="margin-left:134px">exercitation ullamco laboris nisi ut aliquip ex ea commodo consequat. Duis aute irure dolor in</span>
    <span class="intro-line" style="margin-left:112px">reprehenderit in voluptate velit esse cillum dolore eu fugiat nulla pariatur. Excepteur sint occaecat</span>
    <span class="intro-line intro-line--last" style="margin-left:93px">cupidatat non proident, sunt in culpa qui officia deserunt mollit anim id est laborum."</span>
  </p>

  <h2 class="mistake-heading" style="top:360px">1. Not Knowing What You Really Need in ERP Software</h2>
  <p class="mistake-body" style="top:404px">"Lorem ipsum dolor sit amet, consectetur adipiscing elit, sed do eiusmod tempor incididunt ut labore et dolore magna aliqua. Ut enim ad minim veniam, quis nostrud exercitation ullamco laboris nisi ut aliquip ex ea commodo consequat. Duis aute irure dolor in reprehenderit in voluptate velit esse cillum dolore eu fugiat nulla pariatur. Excepteur sint occaecat cupidatat non proident, sunt in culpa qui officia deserunt mollit anim id est laborum."</p>

  <h2 class="mistake-heading" style="top:568px">2. Not Recognizing the Uniqueness of Your Business</h2>
  <p class="mistake-body" style="top:615px">"Lorem ipsum dolor sit amet, consectetur adipiscing elit, sed do eiusmod tempor incididunt ut labore et dolore magna aliqua. Ut enim ad minim veniam, quis nostrud exercitation ullamco laboris nisi ut aliquip ex ea commodo consequat. Duis aute irure dolor in reprehenderit in voluptate velit esse cillum dolore eu fugiat nulla pariatur. Excepteur sint occaecat cupidatat non proident, sunt in culpa qui officia deserunt mollit anim id est laborum."</p>

  <h2 class="mistake-heading" style="top:775px">3. Not Choosing the Most Qualified ERP Software Vendor</h2>
  <p class="mistake-body" style="top:820px">"Lorem ipsum dolor sit amet, consectetur adipiscing elit, sed do eiusmod tempor incididunt ut labore et dolore magna aliqua. Ut enim ad minim veniam, quis nostrud exercitation ullamco laboris nisi ut aliquip ex ea commodo consequat. Duis aute irure dolor in reprehenderit in voluptate velit esse cillum dolore eu fugiat nulla pariatur. Excepteur sint occaecat cupidatat non proident, sunt in culpa qui officia deserunt mollit anim id est laborum."</p>
</main>
</body>
</html>
```